Flyer for a Unique Type of Tax Services

Please refer to the attached sample design for reference. Feel free to change the wording as needed. Here is the project brief:

Objective:
Objective of this flyer is to introduce our services which we are launching soon, which is new of a kind, to our potential customers i.e. online tax return preparation. By looking at the flyer we want our target audience to get convinced of our services and visit our website and register with us. They don’t have to pay anything to register.

Our Competitors:
Currently there are three main options available to get tax returns prepared. First is to buy tax software and get tax return prepared at own, this is the cheapest option. There are studies that suggest that people who are not well aware of tax laws there are chances they miss certain tax refunds by filing returns at their own and potentially lose money. Second option is to go to the local offices of nation-wide tax service companies like P&L Fenwick and Morrow Lindqvist. They open offices only during tax season i.e. Jan through April but they are not available other part of the year and their association with the customers is temporary. Third option is to go to a CPA office which are the most expensive and very few people go for this option.

Weaknesses of the Current Options:
By self-preparing tax returns, there are chances that one can overlook certain tax laws that can provide additional tax credits and exemptions to people and overall they could have got a higher tax refund from the Govt. but they may miss it.
By going to other competitors during the peak time when tax returns are due, there are high chances that they don't have enough time to do research to ensure maximum refunds based on the exact circumstances of the individuals at the peak time as many people come to them during that time. Also they are not available after the tax season to provide them any answers to their questions or provide them tax planning tips to help them save tax in the next season.
By going to the CPA office, they charge a lot of fees and also for any tax advice later during the year, they will charge additional fees.

What we are offering:
We are offering a new option i.e. online tax return preparation through experts. We'll charge the fees competitive to what people are paying to local tax providers. But we will be different than our competitors as we'll be providing value added service if they got their returns prepared through us. Value added services we will be free of any additional cost for our customers who'll get tax return prepared through us.

Our Target Audience:
Our target audience is any person or couple who go to the tax service providers like P&L Fenwick or Morrow Lindqvist to get their tax returns prepared.

How We are Different:
Here is the summary of the unique aspects of our business as compared to the competitors:
- Customers just pay us the price for preparing the annual return and price is comparable and competitive to what they have been paying to other providers.
- Unlike our competitors, we do extensive research to review the circumstances of our customers and explore applicable tax laws to make sure all available tax credits, exemptions, and deductions are taken for our customers, whereas our customers don't usually do such kind of research as during the peak tax season when customers approach them they usually don’t have time to do that kind of research. We start our association with our customers much sooner than the actual due date and this provides us time to do extensive research and we try our best that our customers could get higher tax returns.
- By just getting tax returns prepared through us, we enter into a long-term association with our customers and provide them complimentary tax planning tips throughout the year to help them save tax in the following year
- We are available to our customers year-round to provide complementary answers to any tax related questions without any additional cost e.g. how to save tax when buying a car, whether to buy or lease the care to save tax, for the sole-proprietor business how to save tax by using portion of the home as home-office, how to save tax by using personal car for personal business.
- We also provide answers to other basic financial advise related matters e.g. which insurance product is better, whether full insurance or term-life insurance to chose, how to save for the retirement etc.

Other Details:
Our logo has already been designed and we want the same logo to be used in the flyer. Our website address is: www.FiledRightAdvisor.com (it is still under construction but to get perspective of what we are trying to offer, visit this alternate website that it not final yet but will give an idea: http://www.filedrightadvisor.com/wordpress. Fyi, a video at this link is only a placeholder and not relevant to our services)

Industry/Entity Type

Construction

Requirements
Must have
• Please refer to the sample flyer attached. Feel free to change the design and language.
Should not have
• Please do not put any testimonial on the flyer as reflected in the under construction website.

```html
<!DOCTYPE html>
<html lang="en">
<head>
<meta charset="utf-8">
<title>FiledRight Advisor – Tax Services Flyer</title>
<link href="https://fonts.googleapis.com/css2?family=Quicksand:wght@500;600;700&display=swap" rel="stylesheet">
<style>
  :root {
    --frame-blue: #3b58a6;
    --heading-blue: #2f4b9b;
    --text-dark: #2b2b2b;
    --text-grey: #4a4a4a;
    --accent-orange: #f08a2c;
    --teal: #5bc0cf;
    --band-grey: #c4c4c4;
    --paper: #ffffff;
  }
  * { margin: 0; padding: 0; box-sizing: border-box; }
  html, body { width: 776px; height: 1200px; overflow: hidden; background: var(--frame-blue); }
  .flyer {
    position: relative; width: 776px; height: 1200px;
    background: var(--frame-blue);
    font-family: "Quicksand", sans-serif;
  }
  .panel {
    position: absolute; left: 42px; top: 42px; width: 692px; height: 1113px;
    background: var(--paper); overflow: hidden;
  }
  .hero { position: absolute; left: 0; top: 0; width: 692px; height: 470px; }
  .headline {
    position: absolute; left: 0; top: 500px; width: 692px;
    text-align: center; color: var(--heading-blue);
    font-size: 28px; font-weight: 600; line-height: 39px;
  }
  .questions { position: absolute; left: 28px; top: 652px; width: 650px; list-style: none; }
  .questions li {
    position: relative; padding-left: 0; color: var(--text-dark);
    font-size: 16.5px; font-weight: 500; line-height: 24px; margin-bottom: 19px;
  }
  .questions li::before {
    content: ""; position: absolute; left: -16px; top: 8px; width: 8px; height: 8px;
    background: var(--accent-orange); border: 2px solid var(--heading-blue);
  }
  .questions strong { font-weight: 700; }
  .offer {
    position: absolute; left: 24px; top: 808px; width: 650px;
    text-align: center; color: var(--text-dark);
    font-size: 16.5px; font-weight: 500; line-height: 24px;
  }
  .offer em { color: var(--accent-orange); font-weight: 700; }
  .register {
    position: absolute; left: 0; top: 858px; width: 692px; text-align: center;
    color: var(--accent-orange); font-size: 16.5px; font-weight: 600;
  }
  .register a { color: var(--heading-blue); text-decoration: none; margin-left: 6px; }
  .brand {
    position: absolute; left: 0; top: 920px; width: 692px; text-align: center;
    color: var(--heading-blue); font-size: 26px; font-weight: 700; letter-spacing: 0.5px;
  }
  .brand-mark {
    display: inline-block; width: 14px; height: 14px; border-radius: 50%;
    background: var(--accent-orange); margin-right: 10px; vertical-align: 2px;
  }
  .footer-band { position: absolute; left: 0; top: 979px; width: 692px; height: 134px; }
  .footer-text {
    position: absolute; left: 30px; top: 1001px; width: 636px;
    color: var(--text-grey); font-size: 16.5px; font-weight: 600; line-height: 27px;
    text-align: justify;
  }
</style>
</head>
<body>
<div class="flyer">
  <div class="panel">
    <svg class="hero" viewBox="0 0 692 470" xmlns="http://www.w3.org/2000/svg">
      <defs>
        <linearGradient id="photoTone" x1="0" y1="0" x2="1" y2="1">
          <stop offset="0" stop-color="#5d7f8c"/>
          <stop offset="0.5" stop-color="#8fb0c6"/>
          <stop offset="1" stop-color="#3e5561"/>
        </linearGradient>
      </defs>
      <polygon points="0,0 692,0 692,212 273,430 0,370" fill="url(#photoTone)" role="img" aria-label="Photo of a stressed man at a desk holding his head, with tax forms, a calculator and glasses"/>
      <polygon points="80,385 273,430 692,212 692,95" fill="#5bc0cf" opacity="0.75"/>
      <polygon points="0,392 273,458 692,240 692,212 273,430 0,370" fill="#ffffff"/>
      <polyline points="0,372 273,436 692,218" fill="none" stroke="#f08a2c" stroke-width="5"/>
    </svg>

    <h1 class="headline">Does your Tax Return Preparer<br>has time to do EXTENSIVE RESEARCH<br>for you to get Maximum Refunds?</h1>

    <ul class="questions">
      <li>Do you get year-round <strong>Free Advice</strong> regrding your Tax Related Questions from your existing Tax Service Provider?</li>
      <li>Does your existing <strong>Tax Service Provider</strong> give you complementary Tax Planning Tips throughout the year to help you save tax in the following financial year?</li>
    </ul>

    <p class="offer"><em>If not,</em> then try us as we do provide all these services year-round to our customers who get tax returns prepared through us at no additionaL COST.</p>

    <p class="register">Register now free at: <a href="#">www.filedrightadvisor.com</a></p>

    <div class="brand"><span class="brand-mark"></span>FiledRight Advisor</div>

    <svg class="footer-band" viewBox="0 0 692 134" xmlns="http://www.w3.org/2000/svg">
      <polygon points="0,0 216,0 216,14 500,0 692,0 692,134 0,134" fill="#c4c4c4"/>
    </svg>
    <p class="footer-text">And right away we'll start doing research for you and will be available year-round to answer you tax related queries and we will keep providing you tax planning tips and also provide you guideline on other financial planning matters.</p>
  </div>
</div>
</body>
</html>
```